Wix Design for a Clothing Design Web Marketing Site

We need a Wix design and content (including any images and copy) for a clothing design web storefront, Made 4 Me Now (or made4menow). Rough ideas and content can be found at http://marenoltsby.example-site.com/made4menow.

Made For Me Now is an innovative business concept that combines fashion and entertainment. The business model allows customers to actively participate in the creation of fashion designs/concepts , visualize the garment in the customer’s body in 3D, and buy the physical garment made specially to fit the customer.
The fashion consultant will be able to create the design based on client's desires and test various possibilities (size, fabric, cut, etc..) in front of the customer, using software Venlora (the software is a key component of this business model)
(when developing the website use images from Venlora)
After the design is created, the customer can choose to order the actual piece. The garment will be made according to the created design, the customer measurements.

Target Market(s)

Primarily women from 25 to 45, who are fashion enthusiasts and appreciate fit and exclusivity. They are hedonistic shoppers, who shop for entertainment.
Men (metrosexuals) who are fashion enthusiasts, also hedonistic shoppers.

Industry/Entity Type

Clothing

Font styles to use
Serif
Sans Serif

Requirements
Must have
• Must have a landing page (home) or section, that gives the consumer an idea of what Made 4 Me Now will do for them, an about page or section that tells about the company and product, a how it works page or section that describes how it works (http://marenoltsby.example-site.com/made4menow#!services3/c192y), and page or section about pricing, and a page or section on how to contact us.
Nice to have
• Very modern and clean. The website must be based on the main picture of the studio in the example. If that studio is the store, what will the website look like?
• Colors yellow, grey and white. Use the zig zag in yellow and white. You can change the size of the lines. The zig zagi gives the modern and bold accent. Outfits in pictures must show nicely tailored garments.

```html
<!DOCTYPE html>
<html lang="en">
<head>
<meta charset="utf-8">
<title>Made For Me Now – Price/Packages</title>
<link rel="stylesheet" href="https://fonts.googleapis.com/css2?family=Italiana&family=Roboto+Slab:wght@300;400&family=Roboto+Condensed:wght@400&family=Open+Sans:wght@400;600&family=Alfa+Slab+One&display=swap">
<style>
  :root{
    --yellow:#f2e632;
    --yellow-text:#f4ec3c;
    --ink:#1b1b1b;
    --dark:#202020;
    --darker:#141414;
    --nav:#5f636b;
    --card:#5a5d62;
    --white:#ffffff;
    --text:#333333;
    --muted:#9a9a9a;
  }
  *{box-sizing:border-box;margin:0;padding:0}
  html,body{width:1141px;height:1200px;overflow:hidden}
  body{position:relative;background:var(--dark);font-family:"Open Sans",sans-serif;color:var(--text)}

  .site-header{position:absolute;left:0;top:0;width:1141px;height:170px;background:var(--white)}
  .header-panel{position:absolute;left:0;top:0;width:1141px;height:170px}
  .brand{position:absolute;left:98px;top:20px;width:262px;display:flex;flex-direction:column;align-items:center}
  .brand-disc{width:128px;height:128px;border-radius:50%;background:#bdbab0;border:4px solid #f0f0f0}
  .brand-name{margin-top:-14px;background:var(--white);padding:2px 8px;font-family:"Roboto Slab",serif;font-weight:400;font-size:27px;letter-spacing:1px;color:var(--ink);white-space:nowrap}
  .tagline{position:absolute;left:537px;top:38px;font-family:"Italiana",serif;font-size:46px;line-height:44px;color:var(--white)}

  .main-nav{position:absolute;left:0;top:170px;width:1141px;height:39px;background:var(--nav);display:flex;padding-left:92px}
  .main-nav a{font-family:"Roboto Condensed",sans-serif;font-size:16px;color:var(--white);text-decoration:none;padding:0 26px;line-height:39px}
  .main-nav a.is-active{background:var(--dark)}

  .page-title{position:absolute;left:0;top:209px;width:1141px;height:118px;background:var(--ink);display:flex;align-items:center;justify-content:center;font-family:"Roboto Slab",serif;font-size:30px;color:var(--yellow-text)}

  .chevron-backdrop{position:absolute;left:0;top:327px;width:1141px;height:625px;background:linear-gradient(90deg,#f5d94a,#fbeec8 50%,#f5d94a)}

  .content{position:absolute;left:95px;top:327px;width:938px;height:625px;background:var(--white)}
  .section-heading{position:absolute;left:0;top:28px;width:100%;text-align:center;font-family:"Roboto Slab",serif;font-weight:300;font-size:26px;color:#222}
  .divider{position:absolute;left:304px;top:73px}
  .intro{position:absolute;left:0;top:123px;width:100%;text-align:center;font-size:13px;color:#333}

  .price-cards{position:absolute;left:11px;top:173px;display:flex;gap:8px}
  .price-card{width:300px;height:226px;background:var(--card);color:var(--white);text-align:center;padding:10px 38px 0}
  .price-card h3{font-family:"Roboto Slab",serif;font-weight:300;font-size:20px;line-height:20px;color:var(--yellow-text)}
  .price-card p{font-size:12px;line-height:15px;margin-top:14px}
  .rates{list-style:none;margin-top:22px;font-size:12px;color:var(--yellow-text);text-align:left}
  .rates li{display:flex;line-height:19.5px}
  .rates .leader{flex:1;border-bottom:1px dotted var(--yellow-text);margin:0 2px 6px}

  .feature{position:absolute;top:429px;width:451px;height:196px;background:var(--darker);display:flex}
  .feature--left{left:10px}
  .feature--right{left:476px}
  .feature-body{width:303px;padding:16px 12px;color:var(--white)}
  .feature-body h4{font-family:"Roboto Slab",serif;font-weight:300;font-size:20px;color:var(--yellow-text)}
  .feature-body p{font-size:12px;line-height:19.5px;margin-top:8px}
  .feature-body a{font-size:12px;font-weight:600;color:var(--yellow-text)}
  .feature-photo{flex:1;background:linear-gradient(160deg,#f2e632,#e8d82a)}

  .site-footer{position:absolute;left:0;top:952px;width:1141px;height:199px;background:var(--ink)}
  .footer-col{position:absolute;top:46px;font-size:12px;line-height:19.5px;color:#e4e4e4}
  .footer-col h5{font-family:"Roboto Condensed",sans-serif;font-weight:400;font-size:15px;color:var(--muted);margin-bottom:8px}
  .footer-col ul{list-style:none;padding-left:3px}
  .footer-col a{color:var(--yellow-text);text-decoration:none}
  .col-links{left:128px}
  .col-company{left:315px}
  .col-company address{font-style:normal;padding-left:2px}
  .col-subscribe{left:566px}
  .email-field{width:231px;height:33px;background:var(--white);border:0;font-family:"Roboto Condensed",sans-serif;font-size:12px;color:#999;padding-left:8px;display:block;margin:10px 0 10px}
  .submit{width:92px;height:33px;background:var(--yellow);border:0;font-family:"Roboto Condensed",sans-serif;font-size:14px;color:var(--ink)}
  .footer-brand{position:absolute;left:828px;top:60px;width:190px;display:flex;flex-direction:column;align-items:center}
  .footer-brand-disc{width:100px;height:100px;border-radius:50%;background:#5b5a4c}
  .footer-brand-name{margin-top:-14px;background:#6b6a1e;padding:0 6px;font-family:"Roboto Slab",serif;font-size:19px;color:#2a2a10;white-space:nowrap}

  .copyright{position:absolute;left:0;top:1151px;width:1141px;height:49px;background:var(--darker);display:flex;align-items:center;justify-content:center;font-size:11px;color:#e0e0e0}
</style>
</head>
<body>

<header class="site-header">
  <svg class="header-panel" width="1141" height="170" aria-hidden="true">
    <polygon points="532,0 1141,0 1141,170 458,170" fill="#1d1d1d"/>
  </svg>
  <div class="brand">
    <div class="brand-disc"></div>
    <div class="brand-name">MADE FOR ME NOW</div>
  </div>
  <p class="tagline">Clothes made specially for<br>You and designed by you</p>
</header>

<nav class="main-nav">
  <a href="#">Home</a>
  <a href="#">What is Made For Me Now?</a>
  <a href="#">How It Works?</a>
  <a href="#" class="is-active">Price</a>
  <a href="#">Contact Us</a>
</nav>

<h1 class="page-title">Price/Packages</h1>

<div class="chevron-backdrop" role="img" aria-label="Yellow and white zig-zag background pattern"></div>

<main class="content">
  <h2 class="section-heading">Price List For Each Job Part</h2>
  <svg class="divider" width="330" height="22" aria-hidden="true">
    <line x1="0" y1="11" x2="148" y2="11" stroke="#333" stroke-dasharray="2 1"/>
    <polygon points="165,1 175,11 165,21 155,11" fill="#1b1b1b"/>
    <line x1="182" y1="11" x2="330" y2="11" stroke="#333" stroke-dasharray="2 1"/>
  </svg>
  <p class="intro">Design Services, Actual Garment and Alterations are all charged separately.</p>

  <div class="price-cards">
    <section class="price-card">
      <h3>Full Design</h3>
      <p>The customer convey to the fashion consultant his/her idea through samples (images from magazines, basic drawings).</p>
      <ul class="rates">
        <li>First 2 hours<span class="leader"></span>$200.00</li>
        <li>Additional hour<span class="leader"></span>$50.00</li>
      </ul>
    </section>
    <section class="price-card">
      <h3>Customized design made of existing “blocks”</h3>
      <p>Design made from blocks</p>
      <ul class="rates">
        <li>Hourly rate<span class="leader"></span>$75.00</li>
      </ul>
    </section>
    <section class="price-card">
      <h3>Physical Garment/Outfit – one adjustment included</h3>
      <p>The Prices vary according to complexity of design and fabric</p>
      <ul class="rates">
        <li>Pants<span class="leader"></span>starting at $200.00</li>
        <li>Skirts<span class="leader"></span>starting at $150.00</li>
        <li>Dresses<span class="leader"></span>starting at $200.00</li>
        <li>Suits<span class="leader"></span>starting at $300.00</li>
      </ul>
    </section>
  </div>

  <article class="feature feature--left">
    <div class="feature-body">
      <h4>Lorel ipsum dolor sit amet</h4>
      <p>Donec pulvinar nec orci vel fermentum. Donec venenatis varius tincidunt. Aliquam erat volutpat. Maecenas rhoncus venenatis venenatis. Morbi aliquam nibh eget libero blandit, ac placerat tellus tristique.</p>
      <a href="#">Read More</a>
    </div>
    <div class="feature-photo" role="img" aria-label="Tailored black sheath dress on a yellow background"></div>
  </article>

  <article class="feature feature--right">
    <div class="feature-body">
      <h4>Lorel ipsum dolor sit amet</h4>
      <p>Donec pulvinar nec orci vel fermentum. Donec venenatis varius tincidunt. Aliquam erat volutpat. Maecenas rhoncus venenatis venenatis. Morbi aliquam nibh eget libero blandit, ac placerat tellus tristique.</p>
      <a href="#">Read More</a>
    </div>
    <div class="feature-photo" role="img" aria-label="Navy tailored suit on a mannequin against a yellow background"></div>
  </article>
</main>

<footer class="site-footer">
  <div class="footer-col col-links">
    <h5>QUICK LINKS</h5>
    <ul>
      <li>Home</li>
      <li>What is Made For Me Now?</li>
      <li>How It Works?</li>
      <li>Price</li>
      <li>Contact Us</li>
    </ul>
  </div>
  <div class="footer-col col-company">
    <h5>COMPANY INFO</h5>
    <address>
      58 Alder Row,<br>
      2nd Floor, Room No 310<br>
      Portland, OR<br>
      USA<br>
      Ph: <a href="#">555 0148 372</a><br>
      Email: <a href="#">info@madeformenow.example</a>
    </address>
  </div>
  <div class="footer-col col-subscribe">
    <h5>SUBSCRIBE NEWSLETTER</h5>
    <input class="email-field" type="text" placeholder="Type your email id">
    <button class="submit">SUBMIT</button>
  </div>
  <div class="footer-brand">
    <div class="footer-brand-disc"></div>
    <div class="footer-brand-name">MADE FOR ME NOW</div>
  </div>
</footer>

<div class="copyright">© 2015, All Rights Reserved, Made For Me Now</div>

</body>
</html>
```